The name of my company is Tolmen Refacing LLC and I would like the sub text to say "Cabinet Refacing and Countertops". Have my name Dorian Tolmen, Owner / Sales, contact info: Cell: 360-555-0147 / Email: dorian.tolmen@quenmail.com

Simple, Clean, and Organized. With colors that will appeal to the eye.

Target Market(s)

Houses and Apartments

Industry/Entity Type

Cabinet Refacing

Contact Information for Business Card

Company name and sub text Dorian Tolmen - Owner / Sales, my cell phone number and email

Requirements
Must have
• Business name, my name / position, and my contact info
Nice to have
• Simple. Organized. Appealing to the eye

```html
<!DOCTYPE html>
<html lang="en">
<head>
<meta charset="utf-8">
<title>Tolmen Refacing LLC — Business Card</title>
<link rel="stylesheet" href="https://fonts.googleapis.com/css2?family=Montserrat:wght@300;400;600;700&display=swap">
<style>
  :root {
    --paper: #ffffff;
    --tan: #c6ad99;
    --tan-light: #ddd2c6;
    --brown: #8b5e3c;
    --muted: #c8b4a4;
    --rule: #d9cbbe;
  }
  * { margin: 0; padding: 0; box-sizing: border-box; }
  html, body {
    width: 1200px; height: 699px; overflow: hidden;
    background: var(--paper);
  }
  .card {
    position: relative; width: 1200px; height: 699px;
    background: var(--paper);
    font-family: "Montserrat", sans-serif;
  }
  .brand { position: absolute; left: 112px; top: 136px; }
  .brand-name {
    font-weight: 600; font-size: 39px; color: var(--tan);
    letter-spacing: 0.5px; line-height: 1;
  }
  .brand-tagline {
    margin-top: 14px; font-weight: 400; font-size: 17.5px;
    color: var(--brown); letter-spacing: 1.6px; text-transform: uppercase;
  }
  .brand-rule {
    position: absolute; left: 112px; top: 226px;
    width: 64px; height: 1.5px; background: var(--brown);
  }
  .divider {
    position: absolute; left: 599px; top: 227px;
    width: 1.5px; height: 318px; background: var(--rule);
  }
  .person {
    position: absolute; right: 677px; top: 318px; text-align: right;
  }
  .person-name {
    font-size: 60px; color: var(--brown); line-height: 1; letter-spacing: -2.5px;
  }
  .person-name .first { font-weight: 300; }
  .person-name .last { font-weight: 700; }
  .person-role {
    margin-top: 14px; font-weight: 300; font-size: 27px; color: var(--muted);
    letter-spacing: 3px; text-transform: uppercase;
  }
  .person-role .slash { font-size: 40px; vertical-align: -5px; margin: 0 14px 0 12px; font-weight: 300; }
  .contact { position: absolute; left: 678px; top: 331px; }
  .contact-line {
    font-weight: 300; font-size: 32px; color: var(--brown); line-height: 44px;
  }
  .corner-accent {
    position: absolute; left: 979px; top: 531px;
    width: 221px; height: 168px;
    background: linear-gradient(135deg, var(--tan-light) 0%, var(--tan) 100%);
  }
</style>
</head>
<body>
<div class="card">
  <div class="brand">
    <div class="brand-name">Tolmen Refacing LLC</div>
    <div class="brand-tagline">Cabinet Refacing and Countertops</div>
  </div>
  <div class="brand-rule"></div>
  <div class="divider"></div>

  <div class="person">
    <div class="person-name"><span class="first">Dorian</span><span class="last">Tolmen</span></div>
    <div class="person-role">Owner<span class="slash">/</span>Sales</div>
  </div>

  <div class="contact">
    <div class="contact-line">360-555-0147</div>
    <div class="contact-line">dorian.tolmen@quenmail.com</div>
  </div>

  <div class="corner-accent" role="img" aria-label="Decorative corner motif in warm tan and brown tones"></div>
</div>
</body>
</html>
```